Business Card Design

I do estate sales and would like business card to reflect look and feel of attached logo. I also have copy of logo in .eps and .tif if you need that instead of .jpeg.
Updates

sorry for the delay in reviewing these designs. I will pick one by tomorrow. Here are the absolutes: *must have tagline (we find good homes for your treasures *must use blue and green *must be horizontal *nothing too fancy please submit your best and final. Thanks so much!

Industry/Entity Type

Business

Contact Information for Business Card

Nora Platt

DEALS by NORA
We find good homes for your treasures.

Specializing in one to three-day sales
o (no sale too big or too small)
• Home and garage organizing
• Home Clean-out

Call Nora Platt at 202-555-0187
to schedule.

```html
<!DOCTYPE html>
<html lang="en">
<head>
<meta charset="utf-8">
<title>DEALS by NORA – Business Card</title>
<link href="https://fonts.googleapis.com/css2?family=Encode+Sans+Condensed:wght@300;400;600&display=swap" rel="stylesheet">
<style>
  :root {
    --backdrop: #ecebe6;
    --card-green: #6e7c36;
    --window-white: #ffffff;
    --band-light: #f3f3ee;
    --band-shade: #c9cbc0;
    --logo-green: #6e7c36;
    --accent-blue: #1f6f96;
    --text-white: #ffffff;
  }
  html, body {
    margin: 0;
    padding: 0;
    width: 1200px;
    height: 1000px;
    overflow: hidden;
    background: var(--backdrop);
  }
  .canvas {
    position: relative;
    width: 1200px;
    height: 1000px;
  }
  .card {
    position: absolute;
    left: 100px;
    top: 206px;
    width: 1000px;
    height: 588px;
    background: var(--card-green);
    overflow: hidden;
    font-family: "Encode Sans Condensed", "Arial Narrow", sans-serif;
    box-shadow: 0 6px 18px rgba(0,0,0,0.18);
  }
  .card__band {
    position: absolute;
    inset: 0;
    width: 1000px;
    height: 588px;
  }
  .card__window {
    position: absolute;
    left: 60px;
    top: 55px;
    width: 410px;
    height: 325px;
    background: var(--window-white);
    border-radius: 8px;
    box-shadow: inset 6px 6px 12px rgba(0,0,0,0.22);
    display: flex;
    align-items: center;
    justify-content: center;
    gap: 18px;
  }
  .brand-name {
    margin: 0;
    color: var(--logo-green);
    font-weight: 400;
    text-align: center;
    line-height: 0.95;
    font-size: 96px;
    letter-spacing: 3px;
  }
  .brand-name span { display: block; }
  .brand-name .brand-name__by { font-size: 56px; line-height: 1.1; }
  .brand-mark {
    width: 22px;
    height: 22px;
    background: var(--accent-blue);
    flex: none;
  }
  .card__info {
    position: absolute;
    left: 455px;
    top: 150px;
    width: 510px;
    text-align: center;
    color: var(--text-white);
    font-weight: 300;
    font-size: 30px;
    line-height: 45px;
  }
  .card__info p { margin: 0; height: 45px; white-space: nowrap; }
  .info__title { text-decoration: underline; text-underline-offset: 4px; }
  .info__highlight {
    font-weight: 600;
    font-style: italic;
    font-size: 36px;
    line-height: 0;
  }
</style>
</head>
<body>
<div class="canvas">
  <section class="card" aria-label="DEALS by NORA business card">
    <svg class="card__band" viewBox="0 0 1000 588" aria-hidden="true">
      <defs>
        <linearGradient id="bandFill" x1="0" y1="1" x2="1" y2="0">
          <stop offset="0" stop-color="#c9cbc0"/>
          <stop offset="0.5" stop-color="#f3f3ee"/>
          <stop offset="1" stop-color="#ffffff"/>
        </linearGradient>
      </defs>
      <polygon points="0,384 0,453 727,0 640,0" fill="url(#bandFill)"/>
    </svg>

    <div class="card__window">
      <h1 class="brand-name">
        <span>DEALS</span>
        <span class="brand-name__by">by</span>
        <span>NORA</span>
      </h1>
      <span class="brand-mark" aria-hidden="true"></span>
    </div>

    <div class="card__info">
      <p class="info__title">DEALS by NORA</p>
      <p>We find good homes for your treasures.</p>
      <p>Specializing in one to three-day sales</p>
      <p>(no sale too big or too small)</p>
      <p>• Home and garage organizing</p>
      <p>• Home Clean-out</p>
      <p>Call <span class="info__highlight">Nora Platt</span> at</p>
      <p><span class="info__highlight">202-555-0187</span> to schedule.</p>
    </div>
  </section>
</div>
</body>
</html>
```